Updated Business Cards

We need to update our business cards to reflect new services and employees. We are a luxury vacation rental company in Sandpoint, Idaho. Would also like to make the front facing font easier to read (larger fonts) I love the original logo created for our company and want to use this for the back of the business card created like before - with the dark blue color. See previous files.

Front of the card needs to include:
Employee Name
Title
Phone: 208-555-0147 (ext X)
Address: 418 W. Larkmoor St, Ste 5
Sandpoint, ID 83871
Book Direct: www.RestWillowbay.example

```html
<!DOCTYPE html>
<html lang="en">
<head>
<meta charset="utf-8">
<title>Larkmoor Lodging – Business Card</title>
<link rel="stylesheet" href="https://fonts.googleapis.com/css2?family=Cinzel:wght@400&family=Arimo:wght@400&display=swap">
<style>
  :root {
    --stage: #2f2f31;
    --card-white: #ffffff;
    --navy: #0d2266;
    --navy-ink: #1a2f6e;
    --on-navy: #ffffff;
  }
  * { box-sizing: border-box; margin: 0; padding: 0; }
  html, body {
    width: 1200px;
    height: 689px;
    overflow: hidden;
    background: var(--stage);
  }
  .canvas {
    width: 1200px;
    height: 689px;
    display: flex;
    align-items: center;
    justify-content: center;
    gap: 50px;
  }
  .card {
    width: 525px;
    height: 300px;
    border-radius: 18px;
    box-shadow: 0 14px 30px rgba(0,0,0,0.45);
  }

  /* Back: brand side */
  .card--brand {
    background: var(--card-white);
    display: flex;
    align-items: center;
    justify-content: center;
  }
  .brand {
    display: flex;
    align-items: center;
    gap: 14px;
    color: var(--navy-ink);
    font-family: "Arimo", sans-serif;
    font-weight: 400;
  }
  .brand__mark {
    width: 30px;
    height: 30px;
    background: var(--navy-ink);
    flex: none;
  }
  .brand__name {
    font-size: 36px;
    line-height: 1;
  }

  /* Front: contact side */
  .card--contact {
    background: var(--navy);
    color: var(--on-navy);
    display: flex;
    flex-direction: column;
    justify-content: center;
    align-items: center;
    gap: 22px;
    font-family: "Arimo", sans-serif;
  }
  .person {
    display: flex;
    align-items: center;
    gap: 14px;
  }
  .person__name {
    font-family: "Cinzel", serif;
    font-weight: 400;
    font-size: 28px;
    line-height: 1.1;
  }
  .divider-v {
    width: 1px;
    align-self: stretch;
    background: var(--on-navy);
    opacity: 0.85;
  }
  .person__title { font-size: 16px; }
  .details {
    display: flex;
    align-items: stretch;
    gap: 16px;
    font-size: 15px;
    line-height: 1.5;
  }
  .address { text-align: right; font-style: normal; }
  .contact-line {
    display: flex;
    align-items: center;
    gap: 7px;
  }
  .contact-line svg { width: 13px; height: 13px; fill: var(--on-navy); flex: none; }
</style>
</head>
<body>
<main class="canvas">
  <section class="card card--brand" aria-label="Card back">
    <div class="brand">
      <span class="brand__mark" aria-hidden="true"></span>
      <span class="brand__name">Larkmoor Lodging</span>
    </div>
  </section>

  <section class="card card--contact" aria-label="Card front">
    <div class="person">
      <span class="person__name">Evan Marsh</span>
      <span class="divider-v"></span>
      <span class="person__title">President</span>
    </div>
    <div class="details">
      <address class="address">
        418 W. Larkmoor St, Ste 5<br>
        Sandpoint, ID 83871
      </address>
      <span class="divider-v"></span>
      <div class="contacts">
        <div class="contact-line">
          <svg viewBox="0 0 24 24" aria-hidden="true"><path d="M6.6 10.8a15.1 15.1 0 0 0 6.6 6.6l2.2-2.2c.3-.3.7-.4 1-.2 1.1.4 2.3.6 3.6.6.6 0 1 .4 1 1V20c0 .6-.4 1-1 1C10.6 21 3 13.4 3 4c0-.6.4-1 1-1h3.5c.6 0 1 .4 1 1 0 1.3.2 2.5.6 3.6.1.3 0 .7-.2 1z"/></svg>
          <span>208-555-0147 (ext X)</span>
        </div>
        <div class="contact-line">
          <svg viewBox="0 0 24 24" aria-hidden="true"><path d="M12 2a10 10 0 1 0 0 20 10 10 0 0 0 0-20zm6.9 6h-3a15.7 15.7 0 0 0-1.4-3.6A8 8 0 0 1 18.9 8zM12 4c.8 1.2 1.5 2.5 1.9 4h-3.8c.4-1.5 1.1-2.8 1.9-4zM4.3 14a8 8 0 0 1 0-4h3.4a16.5 16.5 0 0 0 0 4H4.3zm.8 2h3a15.7 15.7 0 0 0 1.4 3.6A8 8 0 0 1 5.1 16zm3-8h-3a8 8 0 0 1 4.4-3.6C8.9 5.5 8.4 6.7 8.1 8zM12 20c-.8-1.2-1.5-2.5-1.9-4h3.8c-.4 1.5-1.1 2.8-1.9 4zm2.3-6H9.7a14.7 14.7 0 0 1 0-4h4.6a14.7 14.7 0 0 1 0 4zm.2 5.6c.6-1.1 1.1-2.3 1.4-3.6h3a8 8 0 0 1-4.4 3.6zm1.8-5.6a16.5 16.5 0 0 0 0-4h3.4a8 8 0 0 1 0 4h-3.4z"/></svg>
          <span>www.RestWillowbay.example</span>
        </div>
      </div>
    </div>
  </section>
</main>
</body>
</html>
```